Tidal Fern Business Cards

We need something new, fun and exciting for business cards. Our current ones are just plain and we need a design that pops. We want name, position held, phone, email on the front, and a 20% discount on the back. I have also uploaded our old business cards creative to see what we are not wanting, and how boring they were and we want something jazzed up from this, cool design and catches people attention.

```html
<!DOCTYPE html>
<html lang="en">
<head>
<meta charset="utf-8">
<title>Tidal Fern Business Cards</title>
<link rel="stylesheet" href="https://fonts.googleapis.com/css2?family=Montserrat:wght@600;800&display=swap">
<style>
  :root {
    --coral: #f07170;
    --navy: #1b3f72;
    --paper: #ffffff;
    --backdrop: #ece7e4;
  }
  * { margin: 0; padding: 0; box-sizing: border-box; }
  html, body {
    width: 1200px;
    height: 1000px;
    overflow: hidden;
    background: var(--backdrop);
    font-family: "Montserrat", sans-serif;
  }
  .canvas {
    position: relative;
    width: 1200px;
    height: 1000px;
  }
  .card {
    position: absolute;
    width: 640px;
    height: 366px;
    overflow: hidden;
    box-shadow: 0 14px 30px rgba(40, 20, 30, 0.18);
  }

  /* Front */
  .card-front {
    left: 90px;
    top: 80px;
    background: var(--coral);
  }
  .front-top {
    position: absolute;
    inset: 0 0 auto 0;
    height: 168px;
    background: var(--paper);
  }
  .brand {
    position: absolute;
    top: 34px;
    right: 70px;
    display: flex;
    align-items: center;
    gap: 14px;
  }
  .brand-dot {
    width: 26px;
    height: 26px;
    border-radius: 50%;
    background: var(--coral);
  }
  .brand-name {
    font-weight: 800;
    font-size: 40px;
    color: var(--navy);
    letter-spacing: 0.5px;
  }
  .person-name {
    position: absolute;
    left: 44px;
    top: 118px;
    font-weight: 800;
    font-size: 46px;
    line-height: 50px;
    letter-spacing: 3px;
    color: var(--coral);
  }
  .person-title {
    position: absolute;
    left: 46px;
    top: 180px;
    font-weight: 800;
    font-size: 18px;
    letter-spacing: 4px;
    text-transform: uppercase;
    color: var(--paper);
  }
  .contact {
    position: absolute;
    left: 46px;
    top: 218px;
    list-style: none;
    color: var(--navy);
    font-weight: 600;
    font-size: 25px;
    line-height: 38px;
    letter-spacing: 2.5px;
  }

  /* Back */
  .card-back {
    left: 470px;
    top: 540px;
    background: var(--navy);
  }
  .back-shapes {
    position: absolute;
    inset: 0;
    width: 640px;
    height: 366px;
  }
  .offer {
    position: absolute;
    left: 0;
    right: 0;
    top: 154px;
    height: 64px;
    line-height: 64px;
    text-align: center;
    font-weight: 800;
    font-size: 36px;
    letter-spacing: 3px;
    color: var(--coral);
  }
</style>
</head>
<body>
<main class="canvas">
  <section class="card card-front" aria-label="Business card front">
    <div class="front-top"></div>
    <div class="brand">
      <span class="brand-dot"></span>
      <span class="brand-name">Tidal Fern</span>
    </div>
    <h1 class="person-name">Rowan Ellery</h1>
    <p class="person-title">Store Manager</p>
    <ul class="contact">
      <li>E: r.ellery@tidalfern.com</li>
      <li>C: (044) 55 3170-2468</li>
      <li>O: (55) 5902-1147</li>
    </ul>
  </section>

  <section class="card card-back" aria-label="Business card back">
    <svg class="back-shapes" viewBox="0 0 640 366" aria-hidden="true">
      <circle cx="600" cy="60" r="60" fill="none" stroke="#f07170" stroke-width="36"/>
      <circle cx="640" cy="330" r="58" fill="#f07170"/>
      <circle cx="120" cy="390" r="130" fill="none" stroke="#f07170" stroke-width="44"/>
      <circle cx="40" cy="40" r="22" fill="#f07170"/>
      <rect x="90" y="140" width="460" height="92" rx="46" fill="#f07170"/>
      <rect x="130" y="154" width="380" height="64" fill="#1b3f72"/>
    </svg>
    <p class="offer">20% DISCOUNT</p>
  </section>
</main>
</body>
</html>
```